Create a Big Data Website that is professional but has a creative flare to it.

I am after a modern business design for a company in the Big Data space however it still needs to have a wow value and something stand out from other corporate websites.
My competitors websites are to give you and idea of content:
www.flintavel.com
www.morvanti.com
www.quarlix4.com.au
www.tessadrine.com
I have uploaded my company Logo so you can use that to make sure it matches your theme.

Target Market(s)

Banks, Insurance Companies, Government, Gas and Energy Companies and Food Manufacturing.

Industry/Entity Type

Consulting

Coding

Coded - Design and coding required

Number of Pages Required

5+ page

Colors

Designer to choose colors to be used in the design.

Requirements
Must have
• Images, Diagrams around Big Data. Usage of information or graphs from sources like Pollwick are fine to use.
Nice to have
• Interactive design use mouse overs, change in text, highlighting information for clear focus.
Should not have
• Cluttered Pages of Informaiton

```html
<!DOCTYPE html>
<html lang="en">
<head>
<meta charset="utf-8">
<title>Veritrix Consulting — Big Data</title>
<link href="https://fonts.googleapis.com/css2?family=Lato:wght@400;700;900&family=Open+Sans:wght@400;600;700&display=swap" rel="stylesheet">
<style>
:root{
  --navy:#12396d;
  --navy-deep:#0c2d5a;
  --blue:#1b8ad8;
  --blue-bright:#2196e6;
  --ink:#1c1c1c;
  --muted:#6a6a6a;
  --grey-bg:#ececec;
  --white:#ffffff;
  --footer:#1b4277;
  --bottom:#2d2d2d;
}
*{margin:0;padding:0;box-sizing:border-box}
html,body{width:1200px;height:3550px;overflow:hidden}
body{position:relative;font-family:"Open Sans",Arial,sans-serif;color:var(--ink);background:var(--white)}
.abs{position:absolute}
h1,h2,h3,h4{font-family:"Lato",Arial,sans-serif}

/* header */
.site-header{top:0;left:0;width:1200px;height:135px;background:linear-gradient(#fbfcfd,#eef1f5)}
.brand{left:100px;top:40px;display:flex;align-items:center;gap:14px}
.brand-mark{width:40px;height:40px;background:var(--navy)}
.brand-name{font-family:"Lato",sans-serif;font-weight:900;font-size:40px;color:var(--navy);letter-spacing:-.5px}
.main-nav{right:135px;top:58px;display:flex;gap:24px;font-family:"Lato",sans-serif;font-weight:700;font-size:14px;color:#2a2a2a;white-space:nowrap}
.main-nav .active{color:var(--navy);border-bottom:2px solid var(--navy);padding-bottom:6px}
.nav-search{left:1086px;top:55px}

/* hero */
.hero{top:135px;left:0;width:1200px;height:540px;background:linear-gradient(120deg,#4a6d9b 0%,#7d9cc3 40%,#9fb5d2 65%,#5f7fab 100%)}
.hero-title{top:360px;left:0;width:1200px;text-align:center;color:var(--white);font-size:36px;font-weight:700}
.hero-sub{top:412px;left:0;width:1200px;text-align:center;color:var(--white);font-size:14px;font-weight:700;line-height:20px}
.btn{display:flex;align-items:center;justify-content:center;font-family:"Lato",sans-serif;font-weight:700;font-size:15px;color:var(--white);text-transform:uppercase}
.btn-solid{background:var(--blue)}
.btn-outline{border:2px solid var(--white)}

/* intro */
.intro-photo{left:94px;top:726px;width:214px;height:214px;border-radius:50%;background:radial-gradient(circle at 50% 45%,#eef3f9,#b8cbe2 70%,#7e9bc1)}
.intro-title{left:433px;top:760px;font-size:34px;font-weight:700;color:#111;letter-spacing:.5px}
.intro-lead{left:435px;top:815px;width:660px;font-size:16px;font-weight:700;line-height:26px}
.intro-body{left:435px;top:880px;width:670px;font-size:13.5px;color:#555;line-height:23px}

/* section headings */
.sec-title{left:0;width:1200px;text-align:center;font-size:36px;font-weight:700}
.sec-sub{left:0;width:1200px;text-align:center;font-size:13px;color:#666}

/* services */
.services{top:1060px;left:0;width:1200px;height:445px;background:var(--grey-bg)}
.svc-card{top:1195px;height:273px;background:var(--white);text-align:center;padding-top:30px}
.svc-card.is-featured{background:var(--navy);color:var(--white)}
.svc-card h3{font-size:16px;font-weight:700;margin:14px 0 22px;letter-spacing:.3px}
.svc-card p{font-size:13.5px;line-height:18px;color:#555;width:220px;margin:0 auto}
.svc-card.is-featured p{color:#d6e2f2}
.read-more{display:inline-flex;align-items:center;gap:6px;font-size:13.5px;font-weight:700;margin-top:10px}

/* analytics */
.analytics{top:1505px;left:0;width:1200px;height:654px;background:linear-gradient(160deg,#1d4d8b 0%,#123f7a 50%,#0b2f62 100%)}
.an-item{color:var(--white);width:300px}
.an-item h4{font-size:16px;font-weight:700;letter-spacing:.3px}
.an-item .rule{width:60px;height:3px;background:var(--white);margin:7px 0 10px}
.an-item p{font-size:13.5px;line-height:18px;color:#e5edf7}
.an-item .read-more{color:var(--white)}
.an-left{text-align:right}
.an-left .rule{margin-left:auto}

/* news */
.news-card{top:2280px;height:343px;background:var(--white);border:1px solid #d8d8d8}
.news-photo{height:205px}
.news-card h4{font-size:17px;font-weight:700;margin:14px 16px 2px;font-family:"Open Sans",sans-serif}
.news-card .tag{font-size:13px;margin-left:16px}
.news-meta{position:absolute;left:16px;right:16px;bottom:32px;display:flex;justify-content:space-between;font-size:13px;color:#666}
.news-meta b{font-weight:400;color:var(--blue)}

/* clients */
.clients{top:2734px;left:0;width:1200px;height:450px;background:#ebebeb}
.client-tile{width:232px;height:118px;background:#e1e1e1;display:flex;align-items:center;justify-content:center;gap:10px;font-family:"Lato",sans-serif;font-size:22px;font-weight:700;color:#5a5a5a}
.client-dot{width:26px;height:26px;border-radius:50%;background:#5a5a5a}

/* footer */
.site-footer{top:3184px;left:0;width:1200px;height:307px;background:var(--footer);color:var(--white)}
.footer-brand{left:0;top:3226px;width:325px;height:72px;background:var(--white);display:flex;align-items:center;padding-left:98px;gap:12px}
.footer-brand .brand-mark{width:30px;height:30px}
.footer-brand .brand-name{font-size:32px}
.footer-about{left:98px;top:3310px;width:250px;font-size:13.5px;line-height:19px;font-weight:600}
.f-head{font-size:13.5px;font-weight:700;letter-spacing:.6px;font-family:"Lato",sans-serif}
.f-links{list-style:none;font-size:13px;line-height:24px}
.f-contact{list-style:none;font-size:14px;line-height:24px}
.f-contact li{display:flex;gap:14px;align-items:flex-start}
.f-contact svg{flex:none;margin-top:5px}
.news-input{left:880px;top:3343px;width:212px;height:34px;background:var(--white);display:flex;align-items:center;justify-content:space-between;padding-left:10px;font-size:11px;color:#999;font-style:italic}
.news-input span.go{width:34px;height:34px;background:var(--blue);display:flex;align-items:center;justify-content:center}
.bottom-bar{top:3491px;left:0;width:1200px;height:59px;background:var(--bottom);color:var(--white)}
.social{right:105px;top:22px;display:flex;gap:24px}
.social span{width:14px;height:14px;border-radius:50%;background:var(--white)}
</style>
</head>
<body>

<header class="abs site-header">
  <div class="abs brand"><span class="brand-mark"></span><span class="brand-name">Veritrix</span></div>
  <nav class="abs main-nav">
    <span class="active">ABOUT</span><span>OUR SERVICES ▾</span><span>BIG DATA ▾</span><span>NEWS</span><span>CLIENTS</span><span>CONTACT</span>
  </nav>
  <svg class="abs nav-search" width="24" height="24" viewBox="0 0 24 24"><circle cx="10" cy="10" r="7" fill="none" stroke="#1b8ad8" stroke-width="3"/><line x1="15" y1="15" x2="22" y2="22" stroke="#1b8ad8" stroke-width="3"/></svg>
</header>

<section class="abs hero" role="img" aria-label="Photo of a hand on a computer mouse beneath floating data charts and binary code, tinted blue"></section>
<h1 class="abs hero-title">Drowning in Data?</h1>
<p class="abs hero-sub">Lorem Ipsum is simply dummy text of the printing and industry.<br>Lorem Ipsum has been the industry's</p>
<a class="abs btn btn-solid" style="left:407px;top:473px;width:185px;height:40px">Get a Quote</a>
<a class="abs btn btn-outline" style="left:608px;top:473px;width:187px;height:40px">Read More</a>

<div class="abs intro-photo" role="img" aria-label="Businessman seen from behind facing a wall of data charts, in a circle"></div>
<h2 class="abs intro-title">BIG DATA</h2>
<p class="abs intro-lead">Lorem Ipsum is simply dummy text of the printing and typesetting industry. Lorem Ipsum has been the industry's.</p>
<p class="abs intro-body">when an unknown printer took a galley of type and scrambled it to make a type specimen book. It has survived not only five centuries, but also the leap into electronic typesetting, remaining essentially unchanged...</p>
<a class="abs btn btn-solid" style="left:435px;top:970px;width:168px;height:43px">Read More</a>

<section class="abs services"></section>
<h2 class="abs sec-title" style="top:1105px">Our Services</h2>
<p class="abs sec-sub" style="top:1152px">Lorem Ipsum is simply dummy text of the printing and industry.</p>

<article class="abs svc-card" style="left:99px;width:299px">
  <svg width="46" height="46" viewBox="0 0 46 46" fill="none" stroke="#222" stroke-width="2.5"><rect x="8" y="4" width="30" height="11" rx="2"/><rect x="8" y="17" width="30" height="11" rx="2"/><rect x="8" y="30" width="30" height="11" rx="2"/><line x1="13" y1="9" x2="22" y2="9"/><line x1="13" y1="22" x2="22" y2="22"/><line x1="13" y1="35" x2="22" y2="35"/></svg>
  <h3>BIG DATA</h3>
  <p>Lorem Ipsum is simply dummy text of the printing and industry has been the industry's</p>
  <span class="read-more">Read More.. <svg width="18" height="18" viewBox="0 0 18 18"><circle cx="9" cy="9" r="7.5" fill="none" stroke="#222" stroke-width="1.5"/><path d="M6 9h6M9.5 6l3 3-3 3" fill="none" stroke="#222" stroke-width="1.5"/></svg></span>
</article>
<article class="abs svc-card is-featured" style="left:447px;width:313px">
  <svg width="46" height="46" viewBox="0 0 46 46" fill="none" stroke="#2196e6" stroke-width="2.5"><circle cx="23" cy="23" r="8"/><g stroke-width="3"><line x1="23" y1="4" x2="23" y2="11"/><line x1="23" y1="35" x2="23" y2="42"/><line x1="4" y1="23" x2="11" y2="23"/><line x1="35" y1="23" x2="42" y2="23"/><line x1="10" y1="10" x2="15" y2="15"/><line x1="31" y1="31" x2="36" y2="36"/><line x1="36" y1="10" x2="31" y2="15"/><line x1="15" y1="31" x2="10" y2="36"/></g></svg>
  <h3>BUSINESS INTELLIGENCE</h3>
  <p>Lorem Ipsum is simply dummy text of the printing and industry has been the industry's</p>
  <span class="read-more">Read More.. <svg width="18" height="18" viewBox="0 0 18 18"><circle cx="9" cy="9" r="7.5" fill="none" stroke="#fff" stroke-width="1.5"/><path d="M6 9h6M9.5 6l3 3-3 3" fill="none" stroke="#fff" stroke-width="1.5"/></svg></span>
</article>
<article class="abs svc-card" style="left:802px;width:303px">
  <svg width="46" height="46" viewBox="0 0 46 46" fill="none" stroke="#222" stroke-width="2.5"><path d="M12 34h23a8 8 0 0 0 0-16 11 11 0 0 0-21-2 9 9 0 0 0-2 18z"/><circle cx="17" cy="26" r="2"/><circle cx="29" cy="26" r="2"/><line x1="19" y1="26" x2="27" y2="26"/></svg>
  <h3>CLOUD</h3>
  <p>Lorem Ipsum is simply dummy text of the printing and industry has been the industry's</p>
  <span class="read-more">Read More.. <svg width="18" height="18" viewBox="0 0 18 18"><circle cx="9" cy="9" r="7.5" fill="none" stroke="#222" stroke-width="1.5"/><path d="M6 9h6M9.5 6l3 3-3 3" fill="none" stroke="#222" stroke-width="1.5"/></svg></span>
</article>

<section class="abs analytics">
  <svg class="abs" style="left:0;top:0" width="1200" height="654" viewBox="0 0 1200 654">
    <line x1="367" y1="128" x2="880" y2="128" stroke="#2196e6" stroke-width="2"/>
    <path d="M620 128 C620 170 580 170 580 213 C580 268 613 263 613 318 C613 372 580 368 580 422 C580 478 613 476 613 531 C613 578 585 600 530 604" fill="none" stroke="#1f8fe0" stroke-width="22" stroke-linecap="round"/>
    <g stroke="#1f8fe0" stroke-width="3">
      <line x1="610" y1="213" x2="774" y2="213"/>
      <line x1="414" y1="318" x2="582" y2="318"/>
      <line x1="610" y1="422" x2="774" y2="422"/>
      <line x1="414" y1="531" x2="582" y2="531"/>
    </g>
    <g fill="#1f8fe0"><circle cx="774" cy="213" r="11"/><circle cx="414" cy="318" r="11"/><circle cx="774" cy="422" r="11"/><circle cx="414" cy="531" r="11"/></g>
    <g fill="#0c2d5a" stroke="#2b9cef" stroke-width="4">
      <circle cx="580" cy="213" r="32"/><circle cx="613" cy="318" r="32"/><circle cx="580" cy="422" r="32"/><circle cx="613" cy="531" r="32"/>
    </g>
    <g fill="none" stroke="#fff" stroke-width="2.2">
      <rect x="566" y="201" width="24" height="17"/><path d="M570 213l5-5 4 3 6-6"/><circle cx="592" cy="221" r="4"/>
      <circle cx="613" cy="314" r="7"/><path d="M610 321v5h6v-5"/>
      <rect x="574" y="410" width="12" height="8"/><rect x="566" y="428" width="10" height="7"/><rect x="584" y="428" width="10" height="7"/><path d="M580 418v5h-9v5M580 423h9v5"/>
      <circle cx="613" cy="531" r="13"/><circle cx="613" cy="527" r="4"/><path d="M606 539a8 6 0 0 1 14 0"/>
    </g>
  </svg>
</section>
<h2 class="abs sec-title" style="top:1553px;color:#fff">Big Data Analytics</h2>
<p class="abs sec-sub" style="top:1600px;color:#fff">Lorem Ipsum is simply dummy text of the printing and industry.</p>

<div class="abs an-item" style="left:802px;top:1698px">
  <h4>PREDICTIVE ANALYTICS</h4><div class="rule"></div>
  <p>Lorem Ipsum is simply dummy text of the printing and typesetting industry. Lorem Ipsum has been the industry's.</p>
  <span class="read-more">Read More.. <svg width="18" height="18" viewBox="0 0 18 18"><circle cx="9" cy="9" r="7.5" fill="none" stroke="#fff" stroke-width="1.5"/><path d="M6 9h6M9.5 6l3 3-3 3" fill="none" stroke="#fff" stroke-width="1.5"/></svg></span>
</div>
<div class="abs an-item an-left" style="left:96px;top:1786px">
  <h4>DATA ENRICHMENT</h4><div class="rule"></div>
  <p>Lorem Ipsum is simply dummy text of the printing and typesetting industry. Lorem Ipsum has been the industry's.</p>
  <span class="read-more">Read More.. <svg width="18" height="18" viewBox="0 0 18 18"><circle cx="9" cy="9" r="7.5" fill="none" stroke="#fff" stroke-width="1.5"/><path d="M6 9h6M9.5 6l3 3-3 3" fill="none" stroke="#fff" stroke-width="1.5"/></svg></span>
</div>
<div class="abs an-item" style="left:802px;top:1906px">
  <h4>DATA GOVERNANCE</h4><div class="rule"></div>
  <p>Lorem Ipsum is simply dummy text of the printing and typesetting industry. Lorem Ipsum has been the industry's.</p>
  <span class="read-more">Read More.. <svg width="18" height="18" viewBox="0 0 18 18"><circle cx="9" cy="9" r="7.5" fill="none" stroke="#fff" stroke-width="1.5"/><path d="M6 9h6M9.5 6l3 3-3 3" fill="none" stroke="#fff" stroke-width="1.5"/></svg></span>
</div>
<div class="abs an-item an-left" style="left:96px;top:1998px">
  <h4>AUTOMATED CRM</h4><div class="rule"></div>
  <p>Lorem Ipsum is simply dummy text of the printing and typesetting industry. Lorem Ipsum has been the industry's.</p>
  <span class="read-more">Read More.. <svg width="18" height="18" viewBox="0 0 18 18"><circle cx="9" cy="9" r="7.5" fill="none" stroke="#fff" stroke-width="1.5"/><path d="M6 9h6M9.5 6l3 3-3 3" fill="none" stroke="#fff" stroke-width="1.5"/></svg></span>
</div>

<h2 class="abs sec-title" style="top:2192px">Latest News</h2>
<p class="abs sec-sub" style="top:2237px">Lorem Ipsum is simply dummy text of the printing and industry.</p>

<article class="abs news-card" style="left:99px;width:299px">
  <div class="news-photo" role="img" aria-label="Glowing globe of connected app symbols over a circuit board" style="background:radial-gradient(circle at 50% 45%,#d4e6f2,#5d8fae 45%,#1f3c52)"></div>
  <h4>Lorem Ipsum is simply ?</h4><div class="tag">Then &amp; Now</div>
  <div class="news-meta"><span>June 20, 2017</span><span>BY <b>JOHN</b></span></div>
</article>
<article class="abs news-card" style="left:457px;width:298px">
  <div class="news-photo" role="img" aria-label="Close-up of a circuit-board chip labelled big data, in blue tones" style="background:linear-gradient(135deg,#7fb1d9,#2d5d8c 55%,#142f4f)"></div>
  <h4>Lorem Ipsum is simply ?</h4><div class="tag">Then &amp; Now</div>
  <div class="news-meta"><span>June 20, 2017</span><span>BY <b>JOHN</b></span></div>
</article>
<article class="abs news-card" style="left:802px;width:301px">
  <div class="news-photo" role="img" aria-label="Businessman from behind facing a wall of world map and charts" style="background:linear-gradient(180deg,#e9f0f8,#a9c0db 60%,#6f8fb7)"></div>
  <h4>Lorem Ipsum is simply ?</h4><div class="tag">Then &amp; Now</div>
  <div class="news-meta"><span>June 20, 2017</span><span>BY <b>JOHN</b></span></div>
</article>
<a class="abs btn btn-solid" style="left:521px;top:2658px;width:165px;height:40px;font-size:14px">View More</a>

<section class="abs clients"></section>
<h2 class="abs sec-title" style="top:2778px">Our Clients</h2>
<p class="abs sec-sub" style="top:2824px">Lorem Ipsum is simply dummy text of the printing and industry.</p>
<div class="abs client-tile" style="left:99px;top:2876px"><span class="client-dot"></span>Kestrova</div>
<div class="abs client-tile" style="left:355px;top:2876px"><span class="client-dot"></span>Kestrova</div>
<div class="abs client-tile" style="left:611px;top:2876px"><span class="client-dot"></span>Kestrova</div>
<div class="abs client-tile" style="left:866px;top:2876px"><span class="client-dot"></span>Kestrova</div>
<div class="abs client-tile" style="left:99px;top:3018px"><span class="client-dot"></span>Kestrova</div>
<div class="abs client-tile" style="left:355px;top:3018px"><span class="client-dot"></span>Kestrova</div>
<div class="abs client-tile" style="left:611px;top:3018px"><span class="client-dot"></span>Kestrova</div>
<div class="abs client-tile" style="left:866px;top:3018px"><span class="client-dot"></span>Kestrova</div>

<footer class="abs site-footer"></footer>
<div class="abs footer-brand"><span class="brand-mark"></span><span class="brand-name">Veritrix</span></div>
<p class="abs footer-about" style="color:#fff">Lorem ipsum dolor sit amet sed conse ctetur adipisicingsed elit sed do elusmod tempor dolore magna aliqua.<br><b style="display:inline-flex;align-items:center;gap:6px">Read More.. <svg width="18" height="18" viewBox="0 0 18 18"><circle cx="9" cy="9" r="7.5" fill="none" stroke="#fff" stroke-width="1.5"/><path d="M6 9h6M9.5 6l3 3-3 3" fill="none" stroke="#fff" stroke-width="1.5"/></svg></b></p>

<h4 class="abs f-head" style="left:419px;top:3235px;color:#fff">QUICK LINKS</h4>
<ul class="abs f-links" style="left:419px;top:3272px;color:#fff">
  <li>› About</li><li>› Our Services</li><li>› Big Data</li><li>› News</li><li>› Client</li><li>› Contact</li>
</ul>

<h4 class="abs f-head" style="left:622px;top:3235px;color:#fff">CONTACT US</h4>
<ul class="abs f-contact" style="left:585px;top:3272px;color:#fff;width:270px">
  <li><svg width="16" height="14" viewBox="0 0 16 14"><path d="M1 7L8 1l7 6M3 6v7h10V6" fill="#fff"/></svg><span>123 ADDRESS,CITY,<br>STATE,ZIP</span></li>
  <li><svg width="16" height="14" viewBox="0 0 16 14"><path d="M3 1h3l1 4-2 1a8 8 0 0 0 4 4l1-2 4 1v3a2 2 0 0 1-2 2A12 12 0 0 1 1 3a2 2 0 0 1 2-2z" fill="#fff"/></svg><span>0 (123) 456-7890</span></li>
  <li><svg width="16" height="14" viewBox="0 0 16 14"><rect x="3" y="0" width="10" height="4" fill="#fff"/><rect x="0" y="5" width="16" height="6" fill="#fff"/><rect x="3" y="9" width="10" height="5" fill="#fff"/></svg><span>0 (123) 456-7890</span></li>
  <li><svg width="16" height="14" viewBox="0 0 16 14"><rect x="0" y="1" width="16" height="12" fill="#fff"/><path d="M0 1l8 6 8-6" fill="none" stroke="#1b4277" stroke-width="1.5"/></svg><span>INFO@VERITRIX.COM</span></li>
  <li><svg width="16" height="14" viewBox="0 0 16 14"><rect x="0" y="0" width="16" height="11" fill="#fff"/><rect x="5" y="12" width="6" height="2" fill="#fff"/></svg><span>WWW.VERITRIX.COM</span></li>
</ul>

<h4 class="abs f-head" style="left:880px;top:3235px;color:#fff">NEWSLETTER SUBSCRIBE</h4>
<p class="abs" style="left:880px;top:3272px;width:220px;font-size:13px;line-height:20px;color:#fff">We will inform you about newset project and promotions.Subscribe to our newsletter.</p>
<div class="abs news-input">Your Email Address<span class="go"><svg width="16" height="12" viewBox="0 0 16 12"><rect x="0" y="0" width="16" height="12" fill="#fff"/><path d="M0 0l8 6 8-6" fill="none" stroke="#1b8ad8" stroke-width="1.5"/></svg></span></div>

<div class="abs bottom-bar">
  <p class="abs" style="left:122px;top:19px;font-size:14px;font-weight:700">© Copyright 2017 Veritrix.All rights Reserved.</p>
  <div class="abs social"><span></span><span></span><span></span><span></span><span></span><span></span></div>
</div>

</body>
</html>
```